Commercial photographer, UAV drone photography & 360 walk-through visuals

I need a business card design that is minimalist but yet pretentiously creative. My target market are architects, designers, advertising agents and marketing managers. It is important to stress that though I am asking for a minimalist design it needs to have creative impact.

Target Market(s)

Architects, interiors designers, web-designers, artists

Contact Information for Business Card

Include my name, mobile [cell] number, email, web page and the company logo. Do not to include a postal address.

Colors

Designer to choose colors to be used in the design.

Requirements
Must have
• The following information is to be included:
• Miles Perrow
• Photographer
• m: 07812 593174
• e: miles@mpframeworks.co.uk
• w: mpframeworks.co.uk

```html
<!DOCTYPE html>
<html lang="en">
<head>
<meta charset="utf-8">
<title>MP Frameworks – Business Card</title>
<link rel="stylesheet" href="https://fonts.googleapis.com/css2?family=Lato:wght@400;700&display=swap">
<style>
  :root {
    --backdrop: #9b9b9b;
    --card-light: #ffffff;
    --card-dark: #231f20;
    --ink: #1a1a1a;
    --rule: #b5b5b5;
  }
  * { margin: 0; padding: 0; box-sizing: border-box; }
  html, body {
    width: 1200px;
    height: 900px;
    overflow: hidden;
    background: var(--backdrop);
  }
  .stage { position: relative; width: 1200px; height: 900px; }

  .card {
    position: absolute;
    width: 477px;
    height: 294px;
    font-family: "Lato", sans-serif;
  }
  .card--front {
    left: 120px; top: 275px;
    background: var(--card-light);
    border-radius: 0 52px 0 52px;
    color: var(--ink);
  }
  .card--back {
    left: 607px; top: 274px;
    background: var(--card-dark);
    border-radius: 52px 0 52px 0;
  }

  .brand {
    position: absolute;
    left: 34px; top: 112px;
    width: 196px;
    display: flex;
    align-items: center;
    gap: 10px;
  }
  .brand__dot {
    width: 14px; height: 14px;
    border-radius: 50%;
    background: var(--ink);
    flex: none;
  }
  .brand__name {
    font-weight: 400;
    font-size: 21px;
    letter-spacing: 2px;
    line-height: 26px;
    color: var(--ink);
  }
  .brand__line { display: block; }

  .divider {
    position: absolute;
    left: 242px; top: 75px;
    width: 1px; height: 145px;
    background: var(--rule);
  }

  .contact {
    position: absolute;
    left: 262px; top: 70px;
    font-size: 13.5px;
    line-height: 17.5px;
  }
  .contact__name {
    font-weight: 700;
    font-size: 18px;
    letter-spacing: 0.4px;
    line-height: 20px;
  }
  .contact__role { margin-bottom: 6px; }
  .contact__list { list-style: none; }
  .contact__item { display: flex; align-items: center; gap: 5px; }
  .contact__item svg { width: 10px; height: 10px; flex: none; fill: var(--ink); }

  .back-brand {
    position: absolute;
    inset: 0;
    display: flex;
    justify-content: center;
    align-items: center;
    font-weight: 400;
    font-size: 26px;
    letter-spacing: 4px;
    color: var(--card-light);
  }
</style>
</head>
<body>
<main class="stage">
  <section class="card card--front">
    <div class="brand">
      <span class="brand__dot"></span>
      <p class="brand__name"><span class="brand__line">MP</span><span class="brand__line">FRAMEWORKS</span></p>
    </div>
    <div class="divider"></div>
    <div class="contact">
      <p class="contact__name">MILES PERROW</p>
      <p class="contact__role">Photographer</p>
      <ul class="contact__list">
        <li class="contact__item">
          <svg viewBox="0 0 10 10" aria-hidden="true"><path d="M2.5 0 H7.5 V10 H2.5 Z M3.4 1 V8 H6.6 V1 Z" fill-rule="evenodd"/></svg>
          07812 593174
        </li>
        <li class="contact__item">
          <svg viewBox="0 0 10 10" aria-hidden="true"><path d="M0 2 H10 V8 H0 Z M0.8 2.6 L5 5.6 L9.2 2.6 Z" fill-rule="evenodd"/></svg>
          miles@mpframeworks.co.uk
        </li>
        <li class="contact__item">
          <svg viewBox="0 0 10 10" aria-hidden="true"><circle cx="5" cy="5" r="4.6"/></svg>
          mpframeworks.co.uk
        </li>
      </ul>
    </div>
  </section>

  <section class="card card--back">
    <p class="back-brand">MP FRAMEWORKS</p>
  </section>
</main>
</body>
</html>
```